Book Cover for Willow Kindred Notes from the Meadow

We have written a book that brings together Notes from the Meadow from a variety of women's voices.
We developed a draft book cover that we like using Canva (attached below). We'd love a book cover that is similar to this image, but looks more professional.
Following are the themes we’d like to depict in the book cover, and in parentheses, how they are represented in the current cover:
1. Divinely feminine (overall cover)
2. Currents of enlightenment (the swirls of light carrying the butterfly)
3. Diversity (a myriad of colors)
4. The solo journey into the unknown (the single butterfly’s flight)
5. Buoyancy and joy (again, the dancing colors and floating butterfly)
6. Boldly feminine (the blue butterfly, set against brush strokes of light)
7. Homage to a dear friend (she loved blue butterflies, the cosmos - this butterfly has hints of the cosmos in her wings, and painting - this background has brush strokes of light).
Book Title, Subtitle, and Editor:
Willow Kindred
Notes from the Meadow
Edited by Mirela Tove
Thank you very much for considering this project!
People who are interested in Women and Spirituality

```html
<!DOCTYPE html>
<html lang="en">
<head>
<meta charset="utf-8">
<title>Willow Kindred — Notes from the Meadow</title>
<link rel="stylesheet" href="https://fonts.googleapis.com/css2?family=Cormorant+Garamond:wght@400;500&family=Allura&display=swap">
<style>
  :root {
    --page-bg: #f4f4f4;
    --cover-bg: #ebebea;
    --cover-shade: #dededd;
    --ink: #141414;
    --lilac: #d9a9dc;
    --violet: #8e8fd6;
    --periwinkle: #a9b4e6;
    --butterfly-blue: #1d6b8f;
    --mist: #cfcfcf;
  }
  * { margin: 0; padding: 0; box-sizing: border-box; }
  html, body {
    width: 1200px;
    height: 800px;
    overflow: hidden;
    background: var(--page-bg);
  }
  .canvas {
    position: relative;
    width: 1200px;
    height: 800px;
  }
  .book-cover {
    position: absolute;
    left: 346px;
    top: 20px;
    width: 508px;
    height: 760px;
    background: radial-gradient(ellipse at 60% 35%, #f2f2f1 0%, var(--cover-bg) 55%, var(--cover-shade) 100%);
    overflow: hidden;
  }
  .cover-title {
    position: absolute;
    top: 34px;
    left: 0;
    width: 100%;
    text-align: center;
    font-family: "Cormorant Garamond", serif;
    font-weight: 400;
    font-size: 84px;
    line-height: 82px;
    letter-spacing: 1px;
    color: var(--ink);
    text-transform: uppercase;
  }
  .cover-subtitle {
    position: absolute;
    top: 206px;
    left: 0;
    width: 100%;
    text-align: center;
    font-family: "Allura", cursive;
    font-size: 44px;
    color: var(--ink);
  }
  .cover-artwork {
    position: absolute;
    left: 0;
    top: 280px;
    width: 100%;
    height: 480px;
    background:
      radial-gradient(ellipse 30% 18% at 62% 40%, rgba(29,107,143,0.85) 0%, rgba(29,107,143,0) 100%),
      radial-gradient(ellipse 40% 30% at 18% 38%, var(--lilac) 0%, rgba(217,169,220,0) 100%),
      radial-gradient(ellipse 45% 32% at 15% 85%, var(--violet) 0%, rgba(142,143,214,0) 100%),
      radial-gradient(ellipse 35% 28% at 48% 65%, var(--periwinkle) 0%, rgba(169,180,230,0) 100%),
      radial-gradient(ellipse 22% 20% at 92% 80%, var(--mist) 0%, rgba(207,207,207,0) 100%);
  }
  .cover-editor {
    position: absolute;
    right: 28px;
    bottom: 30px;
    font-family: "Cormorant Garamond", serif;
    font-weight: 500;
    font-size: 21px;
    color: var(--ink);
  }
</style>
</head>
<body>
  <main class="canvas">
    <section class="book-cover">
      <h1 class="cover-title">Willow<br>Kindred</h1>
      <p class="cover-subtitle">Notes from the Meadow</p>
      <div class="cover-artwork" role="img" aria-label="Watercolour illustration of a blue butterfly with starry wings flying over soft pink, lilac and blue brush-stroke splashes"></div>
      <p class="cover-editor">Edited by Mirela Tove</p>
    </section>
  </main>
</body>
</html>
```